Business Card Design Project

We need a business card design for a new company based in Singapore called 'Bright Harbor Pte Ltd'. We provide personal development training and emotional intelligence workshops. Our slogan is "Actualize your potentials". We will not have a company address on the business card. Only phone number, email address and website address.

Target Market(s)

Adults age 25 to 45 years old.
Mostly working in a job.

Industry/Entity Type

Training

Colors
0255a2
f37123

```html
<!DOCTYPE html>
<html lang="en">
<head>
<meta charset="utf-8">
<title>Bright Harbor – Business Card</title>
<link href="https://fonts.googleapis.com/css2?family=Exo+2:wght@400;500;600&display=swap" rel="stylesheet">
<style>
  :root {
    --page-bg: #e9e6e1;
    --card-bg: #fbfbfb;
    --card-shade: #eeeeee;
    --brand-blue: #0255a2;
    --brand-blue-light: #1b78c8;
    --brand-orange: #f37123;
    --ink: #3a3a3a;
    --ink-soft: #5a5a5a;
    --white: #ffffff;
  }
  * { margin: 0; padding: 0; box-sizing: border-box; }
  html, body { width: 1057px; height: 1200px; overflow: hidden; }
  body {
    background: var(--page-bg);
    font-family: "Exo 2", sans-serif;
    color: var(--ink);
    display: flex;
    flex-direction: column;
    align-items: center;
    justify-content: space-around;
    padding: 30px 0;
  }
  .card {
    position: relative;
    width: 300px;
    height: 525px;
    background: linear-gradient(160deg, var(--card-bg) 0%, var(--card-shade) 100%);
    box-shadow: 0 12px 30px rgba(0,0,0,0.22);
  }
  .brand-dot {
    width: 14px; height: 14px;
    border-radius: 50%;
    background: var(--brand-orange);
    flex: none;
  }
  .brand-name {
    font-weight: 500;
    font-size: 28px;
    color: var(--brand-blue);
    letter-spacing: -0.5px;
    white-space: nowrap;
  }
  /* Front */
  .front-brand {
    position: absolute;
    top: 48px;
    left: 34px;
    display: flex;
    align-items: center;
    gap: 10px;
  }
  .side-strip {
    position: absolute;
    right: 0;
    top: 120px;
    width: 24px;
  }
  .strip-blue {
    height: 140px;
    background: linear-gradient(90deg, var(--brand-blue), var(--brand-blue-light));
  }
  .strip-orange {
    height: 170px;
    background: var(--brand-orange);
    display: flex;
    flex-direction: column;
    align-items: center;
    justify-content: flex-end;
    gap: 18px;
    padding-bottom: 14px;
  }
  .strip-orange svg { width: 12px; height: 12px; }
  .contact {
    position: absolute;
    right: 36px;
    top: 246px;
    text-align: right;
  }
  .person-name { font-size: 17px; font-weight: 500; letter-spacing: 1px; }
  .person-role { font-size: 8px; letter-spacing: 0.8px; color: var(--ink-soft); margin-top: 1px; }
  .contact-list { list-style: none; margin-top: 20px; font-size: 10px; line-height: 30px; color: var(--ink-soft); }
  /* Back */
  .back-brand {
    position: absolute;
    inset: 0;
    display: flex;
    flex-direction: column;
    align-items: center;
    justify-content: center;
    gap: 10px;
  }
  .back-brand-row {
    display: flex;
    align-items: center;
    gap: 12px;
  }
  .back-brand .brand-dot { width: 18px; height: 18px; }
  .back-brand .brand-name { font-size: 30px; }
  .slogan {
    font-size: 13px;
    letter-spacing: 1px;
    color: var(--ink-soft);
  }
</style>
</head>
<body>
  <section class="card card-front">
    <div class="front-brand">
      <span class="brand-dot"></span>
      <span class="brand-name">Bright Harbor</span>
    </div>

    <div class="side-strip">
      <div class="strip-blue"></div>
      <div class="strip-orange">
        <svg viewBox="0 0 12 12" aria-label="phone"><path d="M3 1 L5 3.5 L4 5 Q5.5 7 7 8 L8.5 7 L11 9 L9.5 11 Q4 10 1 2.5 Z" fill="var(--white)"/></svg>
        <svg viewBox="0 0 12 12" aria-label="mobile"><rect x="3" y="0.5" width="6" height="11" rx="1" fill="none" stroke="var(--white)" stroke-width="1.4"/></svg>
        <svg viewBox="0 0 12 12" aria-label="email"><rect x="0.8" y="2.5" width="10.4" height="7" fill="var(--white)"/><path d="M1 3 L6 6.8 L11 3" fill="none" stroke="var(--brand-orange)" stroke-width="1"/></svg>
        <svg viewBox="0 0 12 12" aria-label="website"><circle cx="6" cy="6" r="5" fill="var(--white)"/></svg>
      </div>
    </div>

    <div class="contact">
      <p class="person-name">DANIEL TAN</p>
      <p class="person-role">GENERAL MANAGER</p>
      <ul class="contact-list">
        <li>065 210 4417</li>
        <li>065 210 4418</li>
        <li>hello@brightharbor.sg</li>
        <li>www.brightharbor.sg</li>
      </ul>
    </div>
  </section>

  <section class="card card-back">
    <div class="back-brand">
      <div class="back-brand-row">
        <span class="brand-dot"></span>
        <span class="brand-name">Bright Harbor</span>
      </div>
      <p class="slogan">Actualize your potentials</p>
    </div>
  </section>
</body>
</html>
```